Pebble Pass Business Card

Hello,

Please design a business card for us. We want it to be a plain white card. We want it to be the same style as the flyer. Please make and submit designs, one with each of the four logos. We want the logo in the upper left, and next to the logo we want it to say "The PEBBLE Pass". We have three employees who need cards. I will submit info on each.

Dale Forsyth
Founder
555-318-4072
daleforsyth@pebblepassusa.example
www.pebblepassusa.example

Milo Trench
Founder
555-318-4072
milotrench@pebblepassusa.example
www.pebblepassusa.example

Victor Hale III
Founder
555-318-4072
victorhale@pebblepassusa.example
www.pebblepassusa.example

Industry/Entity Type

Business

```html
<!DOCTYPE html>
<html lang="en">
<head>
<meta charset="utf-8">
<title>Pebble Pass Business Cards</title>
<link rel="stylesheet" href="https://fonts.googleapis.com/css2?family=Quicksand:wght@300;400&family=Cormorant+Garamond:ital,wght@1,500&display=swap">
<style>
  :root {
    --paper: #ffffff;
    --ink: #555555;
    --rule: #6a6a6a;
    --shadow: rgba(0, 0, 0, 0.55);
  }
  * { box-sizing: border-box; margin: 0; padding: 0; }
  html, body { width: 1200px; height: 1000px; overflow: hidden; background: var(--paper); }
  .sheet { position: relative; width: 1200px; height: 1000px; }

  .card {
    position: absolute;
    background: var(--paper);
    box-shadow: 6px 8px 8px var(--shadow);
    color: var(--ink);
  }
  .card--front { left: 15px; top: 60px; width: 553px; height: 322px; }
  .card--dale { left: 614px; top: 58px; width: 556px; height: 324px; --name-w: 231px; --table-w: 472px; }
  .card--victor { left: 17px; top: 459px; width: 551px; height: 321px; --name-w: 287px; --table-w: 468px; }
  .card--milo { left: 621px; top: 460px; width: 549px; height: 320px; --name-w: 228px; --table-w: 466px; }

  /* front */
  .wordmark {
    position: absolute; inset: 0;
    display: flex; align-items: center; justify-content: center;
  }
  .wordmark__name {
    font-family: "Quicksand", sans-serif; font-weight: 400;
    font-size: 40px; letter-spacing: 3px; color: var(--ink);
  }

  /* back */
  .contact-table {
    position: absolute; left: 40px; top: 61px;
    width: var(--table-w); height: 181px;
    display: grid;
    grid-template-columns: 120px calc(var(--name-w) - 120px) 1fr;
    grid-template-rows: 60px 60px 60px;
    border-bottom: 1px solid var(--rule);
  }
  .cell { border-top: 1px solid var(--rule); display: flex; align-items: center; white-space: nowrap; }
  .cell--name {
    grid-column: 1 / 3; grid-row: 1;
    border-right: 1px solid var(--rule);
    flex-direction: column; justify-content: center; line-height: 1;
  }
  .cell--phone { grid-column: 3; grid-row: 1; justify-content: center; }
  .cell--mark { grid-column: 1; grid-row: 2 / 4; border-right: 1px solid var(--rule); justify-content: center; }
  .cell--web { grid-column: 2 / 4; grid-row: 2; justify-content: center; }
  .cell--email { grid-column: 2 / 4; grid-row: 3; justify-content: center; }

  .person {
    font-family: "Quicksand", sans-serif; font-weight: 300;
    font-size: 25px; letter-spacing: 1.5px; text-transform: uppercase;
  }
  .role {
    font-family: "Cormorant Garamond", serif; font-style: italic; font-weight: 500;
    font-size: 13px; letter-spacing: 3px; margin-top: 3px;
  }
  .phone { font-family: "Quicksand", sans-serif; font-weight: 400; font-size: 19px; letter-spacing: 1px; }
  .label {
    font-family: "Quicksand", sans-serif; font-weight: 400;
    font-size: 17px; letter-spacing: 1px; margin-right: 10px;
  }
  .value { font-family: "Cormorant Garamond", serif; font-style: italic; font-weight: 500; font-size: 20px; }
  .value--email { font-size: 19px; }

  .mark__name { font-family: "Quicksand", sans-serif; font-weight: 400; font-size: 19px; letter-spacing: 1px; color: var(--ink); }
</style>
</head>
<body>
<main class="sheet">

  <section class="card card--front">
    <div class="wordmark">
      <span class="wordmark__name">THE PEBBLE PASS</span>
    </div>
  </section>

  <section class="card card--dale">
    <div class="contact-table">
      <div class="cell cell--name"><span class="person">Dale Forsyth</span><span class="role">(Founder)</span></div>
      <div class="cell cell--phone"><span class="phone">555-318-4072</span></div>
      <div class="cell cell--mark"><span class="mark__name">PEBBLE</span></div>
      <div class="cell cell--web"><span class="label">WEB</span><span class="value">www.pebblepassusa.example</span></div>
      <div class="cell cell--email"><span class="label">EMAIL</span><span class="value value--email">daleforsyth@pebblepassusa.example</span></div>
    </div>
  </section>

  <section class="card card--victor">
    <div class="contact-table">
      <div class="cell cell--name"><span class="person">Victor Hale III</span><span class="role">(Founder)</span></div>
      <div class="cell cell--phone"><span class="phone">555-318-4072</span></div>
      <div class="cell cell--mark"><span class="mark__name">PEBBLE</span></div>
      <div class="cell cell--web"><span class="label">WEB</span><span class="value">www.pebblepassusa.example</span></div>
      <div class="cell cell--email"><span class="label">EMAIL</span><span class="value value--email">victorhale@pebblepassusa.example</span></div>
    </div>
  </section>

  <section class="card card--milo">
    <div class="contact-table">
      <div class="cell cell--name"><span class="person">Milo Trench</span><span class="role">(Founder)</span></div>
      <div class="cell cell--phone"><span class="phone">555-318-4072</span></div>
      <div class="cell cell--mark"><span class="mark__name">PEBBLE</span></div>
      <div class="cell cell--web"><span class="label">WEB</span><span class="value">www.pebblepassusa.example</span></div>
      <div class="cell cell--email"><span class="label">EMAIL</span><span class="value value--email">milotrench@pebblepassusa.example</span></div>
    </div>
  </section>

</main>
</body>
</html>
```